Hemp Infused Health Care Products Needs New Labels

Need a label design I can utilize for different products I create, lotion, muscle balm, lip balm, etc. Currently I have a Lumo Vale Soothing Cream label that I created that is rectangle and I want to improve it; more marketable and professional. Create a Circular label also with the words around the circle not straight across This one will be Lumo Vale Muscle Balm. Rec Label is w 5" h 2.5" Circle Label Diameter 2.8"
Target Market(s)
MMJ Dispensaries and online sales. Medical Patients.
Industry/Entity Type
Health And Wellness
Requirements
Must have
- The logo design
- Lumo Vale Soothing Cream
- Lumo Vale Muscle Balm on the round label
Nice to have
- You add some flare to mine to make it more professional and marketable. This will end up being my brand.
Should not have
- No reference or photos of cannabis

```html
<!DOCTYPE html>
<html lang="en">
<head>
<meta charset="utf-8">
<title>Lumo Vale Labels</title>
<link href="https://fonts.googleapis.com/css2?family=Quicksand:wght@500;600;700&family=Raleway:wght@500;800&family=Cinzel:wght@600&display=swap" rel="stylesheet">
<style>
  :root {
    --navy: #23409a;
    --brand: #2d3a9a;
    --ring: #a9c8ea;
    --ring-edge: #8fb2dc;
    --rim: #dde9f6;
    --sky-top: #c9dcf1;
    --sky-mid: #e6eff9;
    --white: #ffffff;
    --body: #2e3a55;
    --green: #6fae3a;
  }
  * { box-sizing: border-box; margin: 0; padding: 0; }
  html, body { width: 1200px; height: 488px; overflow: hidden; background: var(--white); }
  .canvas { position: relative; width: 1200px; height: 488px; font-family: "Quicksand", sans-serif; color: var(--body); }

  .spec-note {
    position: absolute; left: 770px; top: 40px;
    font-family: "Raleway", sans-serif; font-weight: 500; font-size: 19px; color: #222;
  }

  .round-label { position: absolute; left: 36px; top: 66px; width: 404px; height: 404px; }
  .ring-text { font-family: "Raleway", sans-serif; font-weight: 800; font-size: 27px; fill: var(--navy); letter-spacing: 1px; }

  .brand-mark { display: flex; align-items: center; justify-content: center; gap: 8px;
    font-family: "Quicksand", sans-serif; font-weight: 700; color: var(--brand); white-space: nowrap; }
  .brand-dot { width: 14px; height: 14px; border-radius: 50%; background: var(--green); flex: none; }

  .rect-label {
    position: absolute; left: 460px; top: 80px; width: 685px; height: 338px;
    border: 1px solid #c9d6e6; overflow: hidden;
    background: linear-gradient(180deg, var(--sky-top) 0%, var(--sky-mid) 45%, var(--white) 75%);
  }
  .rect-wave { position: absolute; left: 0; top: 0; width: 685px; height: 338px; }

  .rect-logo { position: absolute; left: 220px; top: 80px; width: 240px; height: 44px; font-size: 27px; }

  .usage { position: absolute; left: 30px; top: 72px; width: 145px; font-size: 12.5px; line-height: 1.5; text-align: center; }
  .ingredients { position: absolute; left: 512px; top: 60px; width: 138px; font-size: 12.5px; line-height: 1.45; text-align: center; }

  .product-title { position: absolute; left: 138px; top: 212px; width: 400px; text-align: center; color: var(--navy); font-family: "Raleway", sans-serif; }
  .product-title .line-1 { font-weight: 800; font-size: 44px; letter-spacing: 2px; line-height: 1; }
  .product-title .line-2 { font-weight: 500; font-size: 27px; letter-spacing: 4px; line-height: 1.2; }
  .product-title .tagline { font-family: "Cinzel", serif; font-weight: 600; font-size: 11px; letter-spacing: .5px; margin-top: 6px; line-height: 1.35; }

  .volume { position: absolute; left: 566px; top: 292px; font-family: "Raleway", sans-serif; font-weight: 500; font-size: 14px; color: #222; letter-spacing: 1px; }
</style>
</head>
<body>
<main class="canvas">
  <p class="spec-note">w 5" h 2.5" Circle Label Diameter 2.8"</p>

  <svg class="round-label" viewBox="0 0 364 364" aria-label="Lumo Vale Muscle Balm round label">
    <defs>
      <path id="arc-top" d="M 60 182 A 122 122 0 0 1 304 182"/>
      <path id="arc-bottom" d="M 34 182 A 148 148 0 0 0 330 182"/>
    </defs>
    <circle cx="182" cy="182" r="178" fill="var(--rim)" stroke="var(--ring-edge)" stroke-width="2"/>
    <circle cx="182" cy="182" r="160" fill="var(--ring)" stroke="var(--ring-edge)" stroke-width="2"/>
    <circle cx="182" cy="182" r="110" fill="var(--white)" stroke="var(--ring-edge)" stroke-width="2"/>
    <text class="ring-text"><textPath href="#arc-top" startOffset="50%" text-anchor="middle">LUMO VALE MUSCLE BALM</textPath></text>
    <text class="ring-text"><textPath href="#arc-bottom" startOffset="50%" text-anchor="middle">LUMO VALE MUSCLE BALM</textPath></text>
    <foreignObject x="82" y="152" width="200" height="60">
      <div xmlns="http://www.w3.org/1999/xhtml" class="brand-mark" style="font-size:22px;height:60px;">
        <span class="brand-dot"></span><span>Tavira Healers</span>
      </div>
    </foreignObject>
  </svg>

  <section class="rect-label" aria-label="Lumo Vale Soothing Cream rectangular label">
    <svg class="rect-wave" viewBox="0 0 685 338" preserveAspectRatio="none" aria-hidden="true">
      <path d="M0 170 C 180 225, 420 140, 685 205 L685 338 L0 338 Z" fill="var(--white)"/>
      <path d="M0 162 C 180 217, 420 132, 685 196" fill="none" stroke="#b7cfea" stroke-width="2"/>
      <path d="M0 152 C 180 207, 420 122, 685 185" fill="none" stroke="#d3e2f3" stroke-width="1.5"/>
      <path d="M0 142 C 180 197, 420 112, 685 174" fill="none" stroke="#d3e2f3" stroke-width="1"/>
    </svg>

    <div class="rect-logo brand-mark"><span class="brand-dot"></span><span>Tavira Healers</span></div>

    <p class="usage">To Use: Apply a small amount to affected area as needed.<br>For External Use Only</p>

    <p class="ingredients">Active Ingredient: Hemp Infused Organic Coconut Oil<br>Essential Oils: Peppermint, Lavender, Frankincense, Wild Orange, Ginger, Rosemary</p>

    <div class="product-title">
      <p class="line-1">LUMO VALE</p>
      <p class="line-2">SOOTHING CREAM</p>
      <p class="tagline">Made with Organic Pure Therapeutic Grade<br>ESSENTIAL OILS</p>
    </div>

    <p class="volume">4 FL OZ</p>
  </section>
</main>
</body>
</html>
```